Flyer to advertise gutter cleaning throughout the Autumn and winter monthss

I need a new flyer to advertise gutter and driveway cleaning, roof and gutter repairs.

I am an experienced licensed Plumber and Gasfitter looking to broaden my scope of work to gutter cleaning. I am experienced in cleaning gutter and live in a area with large gum trees. I wont something that's clear, eye catching but not too busy.

Flyer requirements: Free roof inspection - no obligation. Gutter Cleaning from $199. Pictures of men using blower or hands to clean roof gutters (no obvious faces) to be included. Australian looking houses.

A mention that 'All general plumbing maintenance' is offered as other services but not too much wording about this as the target is for gutter cleaning.

Phone number: 0427 386 915 (in this format)
Business Name: Bellvane Plumbing & Gasfitting
License: 3174520
ABN: 71904352816
Web: http://bellvaneplumbing.example-site.net/

Target Market(s)

Elderly - busy working class

Industry/Entity Type

Plumber

Font styles to use
Sans Serif

Colors
0355a3
fbed22
ec1f27
f78f20

Requirements
Must have
• Roof Gutter Cleaning pictures
• Men in protective clothing if possible
Nice to have
• More information:
• Prevent against flooding, mold, rust, rotting and corrosion now!
• Gutter Cleaning Services
• • Remove leaves, sticks, and other debris
• • Clear away clogs
• • Test your downpipes
• • Pinpoint any gutter issues
• • Repair gutter
• With regular service, you can count on your property to be well-protected no matter what the forecast!
Should not have
• Houses that don't look Australian

```html
<!DOCTYPE html>
<html lang="en">
<head>
<meta charset="utf-8">
<title>Bellvane Plumbing &amp; Gasfitting – Gutter Cleaning Flyer</title>
<link rel="stylesheet" href="https://fonts.googleapis.com/css2?family=Jost:wght@400;500;700;800&display=swap">
<style>
  :root {
    --backdrop: #e9e9ec;
    --paper: #ffffff;
    --haze-top: #6f6fa3;
    --haze-mid: #c9c9dc;
    --ink: #1f1f22;
    --panel-dark: #262626;
    --brand-red: #c8103a;
    --ring-red: #e8173f;
    --ring-yellow: #fde95f;
    --ring-blue: #2a3f9c;
    --price-blue: #2b3d98;
    --white: #ffffff;
  }
  * { box-sizing: border-box; margin: 0; padding: 0; }
  html, body {
    width: 1200px; height: 1200px; overflow: hidden;
    background: var(--backdrop);
    font-family: "Jost", Arial, sans-serif;
  }
  .flyer {
    position: absolute; left: 184px; top: 30px;
    width: 832px; height: 1140px;
    background: linear-gradient(180deg, var(--haze-top) 0%, var(--haze-mid) 30%, var(--paper) 55%, var(--paper) 100%);
    overflow: hidden;
  }
  .emblem { position: absolute; left: 165px; top: 45px; width: 520px; height: 520px; }
  .business-name {
    position: absolute; left: 0; width: 100%; top: 576px;
    text-align: center; color: var(--ink);
    font-weight: 800; font-size: 45px; line-height: 51px; letter-spacing: 1px;
    text-transform: uppercase;
  }
  .offer-ribbon {
    position: absolute; left: 51px; top: 701px; width: 726px; height: 115px;
    background: var(--brand-red);
    clip-path: polygon(0 0, 100% 0, 89.5% 50%, 100% 100%, 0 100%, 9.1% 50%);
    display: flex; flex-direction: column; align-items: center; justify-content: center;
    color: var(--white); font-weight: 500; font-size: 43px; line-height: 45px;
    text-transform: uppercase; letter-spacing: 0.5px;
  }
  .service-box {
    position: absolute; top: 838px; height: 138px; width: 224px;
    background: var(--panel-dark); color: var(--white);
    display: flex; flex-direction: column; align-items: center; justify-content: center;
  }
  .service-box .service-title { font-weight: 800; font-size: 44px; line-height: 46px; }
  .service-box.driveway .service-title { font-size: 35px; line-height: 42px; }
  .service-box .service-sub { font-size: 21px; font-weight: 500; text-transform: uppercase; margin-top: 6px; }
  .gutter { left: 51px; }
  .driveway { left: 421px; }
  .price-box {
    position: absolute; top: 838px; height: 138px; width: 114px;
    background: var(--price-blue); color: var(--white);
    display: flex; align-items: center; justify-content: center;
  }
  .price-box span { transform: rotate(-90deg); font-weight: 800; font-size: 42px; white-space: nowrap; }
  .price-gutter { left: 290px; }
  .price-driveway { left: 663px; }
  .contact {
    position: absolute; left: 0; width: 100%; top: 996px;
    text-align: center; color: var(--ink);
    font-weight: 800; font-size: 38px; line-height: 44px;
  }
  .contact .phone-line { display: flex; align-items: center; justify-content: center; gap: 8px; }
  .phone-icon { width: 38px; height: 40px; }
</style>
</head>
<body>
  <main class="flyer">
    <svg class="emblem" viewBox="0 0 520 520" xmlns="http://www.w3.org/2000/svg">
      <defs>
        <linearGradient id="photoTones" x1="0" y1="0" x2="0" y2="1">
          <stop offset="0" stop-color="#e9eef2"/>
          <stop offset="0.35" stop-color="#8a5a48"/>
          <stop offset="0.6" stop-color="#7a4f40"/>
          <stop offset="0.75" stop-color="#d9c06a"/>
          <stop offset="1" stop-color="#b99e4e"/>
        </linearGradient>
      </defs>
      <circle cx="260" cy="260" r="194" fill="url(#photoTones)" role="img" aria-label="Photo of a worker in protective gear pressure-cleaning a tiled roof above the gutter"/>
      <path d="M338 474 A228 228 0 0 1 73.3 129.2" fill="none" stroke="var(--ring-blue)" stroke-width="34"/>
      <path d="M374 62.5 A228 228 0 0 1 182 474.3" fill="none" stroke="var(--ring-yellow)" stroke-width="34"/>
      <path d="M45.7 182 A228 228 0 0 1 484.5 220.4" fill="none" stroke="var(--ring-red)" stroke-width="34"/>
    </svg>

    <h1 class="business-name">Bellvane Plumbing<br>&amp; Gasfitting</h1>

    <div class="offer-ribbon">
      <span>Free Roof Inspection</span>
      <span>No Obligation</span>
    </div>

    <div class="service-box gutter">
      <span class="service-title">GUTTER</span>
      <span class="service-sub">Cleaning from</span>
    </div>
    <div class="price-box price-gutter"><span>$199</span></div>

    <div class="service-box driveway">
      <span class="service-title">DRIVEWAY</span>
      <span class="service-sub">Cleaning from</span>
    </div>
    <div class="price-box price-driveway"><span>$299</span></div>

    <div class="contact">
      <div class="phone-line">
        <svg class="phone-icon" viewBox="0 0 38 40" xmlns="http://www.w3.org/2000/svg" aria-hidden="true">
          <rect x="1" y="1" width="36" height="38" rx="7" fill="var(--ink)"/>
          <path d="M13 8 l5 0 l1 7 l-3 2 c1 4 3 7 6 9 l3 -2 l6 2 l-1 5 c-10 1 -19 -9 -19 -21 z" fill="var(--white)"/>
        </svg>
        <span>0427 386 915 I LICENSE: 3174520</span>
      </div>
      <div>ABN: 71904352816</div>
    </div>
  </main>
</body>
</html>
```